Food Processing Economic Development Postcard

Corran Ridge Economic Development Council (CREDC) is one of the leading economic development agencies in New Mexico. We serve all communities of Doña Ana County’s 3,815 sq. miles of land, located in southern New Mexico, adjacent to El Paso and Mexico. The purpose of this postcard is to recruit potential food processing companies located in California to explore the potential expanding to Doña Ana County. We are looking for a two-sided, color oversize postcard (8.52” x 5.47”) with address section to help promote our region.

Our initial design concept for the front would be a child riding a roller coaster afraid with a main message stating something along the lines of “Having trouble stomaching the California Business Climate?” and a second line saying “Shouldn’t doing business be more enchanting….” Our company logo would also need to be placed in the front somewhere.

The back of the postcard would show some sort of excited/happy child about food with the main message being “Let us show you a better place!” Our company contact information should be placed somewhere on the back

Alternatively imagery could show a sad or crying child standing in the rain or other bad weather. Message could include “tired of the business climate in California?” Second image on reverse side could show child playing in the sun with the same tagline “Shouldn’t doing business be more enchanting”.

These are ideas and we encourage the creativity of the design community in suggestions on getting this message through.

The following information would need to be added on the back postcard.
Halvard & Pike recently ranked New Mexico “Best in the West for Manufacturing” Doña Ana County has the following to offer your company.

Doña Ana County is home to 2,184 (UP 24% from 2007) farms with over 659,000 acres of farmland (Up 12% since 2007). We are one of the top producers in the U.S. for pecans and chile, the second largest vegetable producer in NM, and home to one of the top five largest dairies in the country.

Location (bulleted list)
• Equidistant between ports of Marlow Sound and Brackenford
• 2 Interstates (I-10, I-25)
• 2 railroads (TKRW, Granite Meridian)
• Gateway Crossing with Mexico and a Frontier Heavy Freight Zone
• 340 Days of Sunshine, low humidity, and rare inclement weather

Potential Incentives (bulleted list)
• Work Finalist Grant
• On the Job Training
• Land Trade for Job Creation
• Property Tax Abatements and low property assessments

Companies that know Already (bulleted list)
• Brevik Foods
• Talbridge Enterprises
• Tosk Chile
• Orrin Hill Winery
• Pureloxa
• Merrow Whole Foods
• Kestrel Cold Storage
• J&T Dairy
• Birch Hollow Pecans

We are very open to other artistic ideas to get our message across beyond visual concepts of roller coaster rides as long as it depicts or translates the message of a better opportunity and business climate in Doña Ana County than their current location. The facts on the back must stay the same but the main tagline message on front and back can be replaced to better fit the images chosen for the postcard. Also note that the tagline originally proposed plays on New Mexico’s nickname “Land of Enchantment.” Special symbolism that illustrates creative messaging that can incorporate local community or statewide meanings in favor of New Mexico will be given preference, but this is not a requirement.

Company contact info.
CREDC
800-555-0147
corranridgeplex.example/Food

Also attached is the company logo (CREDC) to be used in the design and a couple images to give an idea of where we are located. These images may be used in your design to highlight our location or you may choose to use something different. We have also attached a secondary right space logo which we occasionally use on some of our publications with you may choose to use in your designs.

```html
<!DOCTYPE html>
<html lang="en">
<head>
<meta charset="utf-8">
<title>CREDC Food Processing Postcard</title>
<link href="https://fonts.googleapis.com/css2?family=Oswald:wght@400;500&family=Roboto+Condensed:wght@400;700&family=Montserrat:wght@600;700&display=swap" rel="stylesheet">
<style>
:root{
  --stage:#3a3a3a;
  --gold:#e8a92a;
  --maroon:#8a1c24;
  --ink:#222222;
  --paper:#ffffff;
  --panel:#f2f2f2;
  --rule:#b9b9b9;
}
*{margin:0;padding:0;box-sizing:border-box}
html,body{width:1000px;height:1200px;overflow:hidden}
body{background:var(--stage);position:relative;font-family:"Roboto Condensed",sans-serif;color:var(--ink)}

/* ---------- front ---------- */
.card-front{position:absolute;left:70px;top:42px;width:838px;height:538px;background:var(--gold)}
.hero-photo{position:absolute;left:20px;top:14px;width:800px;height:508px;
  background:radial-gradient(ellipse at 30% 50%,#d59a86 0%,#a9746a 35%,#5d5050 70%,#3f4a5a 100%)}
.speech-bubble{position:absolute;left:0;top:0;width:838px;height:538px}
.bubble-copy{position:absolute;left:420px;top:30px;width:400px;text-align:center;font-family:"Oswald",sans-serif}
.bubble-lead{font-size:31px;color:var(--ink);line-height:1.15}
.bubble-head{font-size:38px;color:var(--maroon);line-height:1.1;font-weight:500}
.bubble-rule{width:300px;margin:6px auto 6px;border-top:2px dotted var(--ink)}
.bubble-sub{font-size:26px;color:var(--paper);line-height:1.3}
.bubble-sub em{font-style:normal;color:var(--maroon)}
.front-brand{position:absolute;left:48px;top:404px;display:flex;align-items:center;gap:8px}
.brand-mark{width:22px;height:22px;background:var(--gold);border-radius:50%}
.brand-name{font-family:"Oswald",sans-serif;font-weight:500;font-size:40px;color:var(--gold);line-height:1}
.brand-url{font-family:"Roboto Condensed",sans-serif;font-size:11px;color:var(--paper);margin-top:2px}
.front-phone{position:absolute;left:518px;top:452px;width:302px;height:48px;background:var(--maroon);
  display:flex;align-items:center;justify-content:center;gap:8px;font-family:"Montserrat",sans-serif;font-weight:700;font-size:29px;color:var(--gold)}
.front-phone svg{width:22px;height:22px}

/* ---------- back ---------- */
.card-back{position:absolute;left:70px;top:614px;width:840px;height:538px;background:var(--paper)}
.info-side{position:absolute;left:0;top:0;width:525px;height:538px;background:var(--panel);
  clip-path:polygon(0 0,525px 0,445px 100%,0 100%)}
.kid-photo{position:absolute;left:0;top:0;width:215px;height:136px;
  background:linear-gradient(135deg,#e9d6b8 0%,#c89a6c 45%,#5c7fb0 100%)}
.headline-panel{position:absolute;left:215px;top:0;width:320px;height:136px;background:var(--gold);
  font-family:"Oswald",sans-serif;text-align:center;padding-top:26px;padding-right:40px}
.headline-small{font-size:30px;color:var(--ink);line-height:1.15}
.headline-big{font-size:36px;color:var(--maroon);line-height:1.2}
.intro{position:absolute;left:12px;top:146px;width:478px;font-size:12px;line-height:1.42}
.intro strong{color:var(--maroon);font-weight:700}
.fact-col{position:absolute;top:248px;font-size:11.5px;line-height:1.42}
.fact-col h3{font-family:"Oswald",sans-serif;font-weight:400;font-size:14px;text-decoration:underline;margin-bottom:2px;color:var(--ink)}
.fact-col ul{list-style:none;color:var(--maroon)}
.fact-col li{padding-left:9px;text-indent:-9px}
.fact-col li::before{content:"• "}
.col-location{left:26px;width:268px}
.col-incentives{left:296px;width:164px;padding-left:10px;border-left:1px dotted var(--ink);height:130px}
.partners{position:absolute;left:10px;top:398px;width:452px;text-align:center}
.partners h3{font-family:"Oswald",sans-serif;font-weight:400;font-size:14px;text-decoration:underline;margin-bottom:1px}
.partners ul{list-style:none;font-size:11.5px;line-height:1.5;color:var(--maroon);white-space:nowrap}
.partners li{display:inline;margin:0 4px}
.partners li::before{content:"•"}
.contact-band{position:absolute;left:0;top:458px;width:525px;height:80px;background:var(--maroon);border-top:5px solid var(--gold);padding:8px 0 0 84px}
.contact-phone{display:flex;align-items:center;gap:6px;font-family:"Montserrat",sans-serif;font-weight:700;font-size:29px;color:var(--gold);line-height:1.1}
.contact-web{display:flex;align-items:center;gap:6px;font-family:"Montserrat",sans-serif;font-weight:600;font-size:16px;color:var(--gold);margin-top:4px;margin-left:-30px}
.contact-phone svg{width:22px;height:22px}
.contact-web svg{width:16px;height:16px}
.divider-stripe{position:absolute;left:0;top:0;width:560px;height:538px}

.stamp-box{position:absolute;left:712px;top:21px;width:102px;height:130px;border:1px solid var(--rule)}
.address-line{position:absolute;left:537px;width:275px;border-top:1px solid var(--rule)}
.line-1{top:233px}.line-2{top:299px}
.partner-badge{position:absolute;left:540px;top:366px;width:62px;height:70px;background:var(--gold);border-radius:4px}
.back-brand{position:absolute;left:513px;top:462px;display:flex;align-items:center;gap:6px}
.back-brand .brand-name{font-size:34px}
.back-brand .brand-mark{width:18px;height:18px}
.back-brand .brand-url{color:var(--ink);font-size:10px}
.location-map{position:absolute;left:652px;top:368px;width:158px;height:158px;border:2px solid var(--ink);
  background:linear-gradient(160deg,#f4f4f4 0%,#e6e6e6 55%,#d9cfcf 100%)}
</style>
</head>
<body>

<section class="card-front">
  <div class="hero-photo" role="img" aria-label="Frightened child screaming on a roller coaster with an adult rider behind"></div>
  <svg class="speech-bubble" viewBox="0 0 838 538" aria-hidden="true">
    <path d="M420 14 C395 90 400 170 470 230 C510 262 555 275 585 280 L572 310 L620 278 C690 268 760 255 820 235 L820 14 Z" fill="var(--gold)"/>
  </svg>
  <div class="bubble-copy">
    <p class="bubble-lead">Having Trouble Stomaching</p>
    <p class="bubble-head">The California<br>Business Climate?”</p>
    <div class="bubble-rule"></div>
    <p class="bubble-sub">Shouldn’t doing business<br>be more <em>Enchanting</em>….</p>
  </div>
  <div class="front-brand">
    <span class="brand-mark"></span>
    <div><p class="brand-name">CREDC</p><p class="brand-url">corranridgeplex.example</p></div>
  </div>
  <div class="front-phone">
    <svg viewBox="0 0 24 24" aria-hidden="true"><path d="M6.6 10.8a15 15 0 0 0 6.6 6.6l2.2-2.2a1 1 0 0 1 1-.25 11.4 11.4 0 0 0 3.6.6 1 1 0 0 1 1 1V20a1 1 0 0 1-1 1A17 17 0 0 1 3 4a1 1 0 0 1 1-1h3.5a1 1 0 0 1 1 1c0 1.250.2 2.45.6 3.6a1 1 0 0 1-.25 1z" fill="var(--paper)"/></svg>
    800-555-0147
  </div>
</section>

<section class="card-back">
  <div class="info-side">
    <div class="kid-photo" role="img" aria-label="Happy child eating breakfast at a table"></div>
    <div class="headline-panel">
      <p class="headline-small">Let us show you</p>
      <p class="headline-big">A BETTER PLACE!</p>
    </div>
    <p class="intro">Halvard &amp; Pike recently ranked New Mexico <strong>“Best in the West for Manufacturing”</strong> Doña Ana County has the following to offer your company.<br>
    Doña Ana County is home to 2,184 <strong>(UP 24% from 2007)</strong> farms with over 659,000 acres of farmland <strong>(Up 12% since 2007)</strong>. We are one of the top producers in the U.S. for <strong>Pecans and Chile</strong>, the <strong>second largest vegetable producer in NM</strong>, and home to one of the <strong>top five largest dairies in the country</strong>.</p>
    <div class="fact-col col-location">
      <h3>Location</h3>
      <ul>
        <li>Equidistant between ports of Marlow Sound and Brackenford</li>
        <li>2 Interstates (I-10, I-25)</li>
        <li>2 railroads (TKRW, Granite Meridian)</li>
        <li>Gateway Crossing with Mexico and a Frontier Heavy Freight Zone</li>
        <li>340 Days of Sunshine, low humidity, and rare inclement weather</li>
      </ul>
    </div>
    <div class="fact-col col-incentives">
      <h3>Potential Incentives</h3>
      <ul>
        <li>Work Finalist Grant</li>
        <li>On the Job Training</li>
        <li>Land Trade for Job Creation</li>
        <li>Property Tax Abatements and low property assessments</li>
      </ul>
    </div>
    <div class="partners">
      <h3>Companies that know Already</h3>
      <ul>
        <li>Brevik Foods</li><li>Talbridge Enterprises</li><li>Tosk Chile</li><li>Orrin Hill Winery</li><li>Pureloxa</li>
      </ul>
      <ul>
        <li>Merrow Whole Foods</li><li>Kestrel Cold Storage</li><li>J&amp;T Dairy</li><li>Birch Hollow Pecans</li>
      </ul>
    </div>
    <div class="contact-band">
      <p class="contact-phone">
        <svg viewBox="0 0 24 24" aria-hidden="true"><path d="M6.6 10.8a15 15 0 0 0 6.6 6.6l2.2-2.2a1 1 0 0 1 1-.25 11.4 11.4 0 0 0 3.6.6 1 1 0 0 1 1 1V20a1 1 0 0 1-1 1A17 17 0 0 1 3 4a1 1 0 0 1 1-1h3.5a1 1 0 0 1 1 1c0 1.25.2 2.45.6 3.6a1 1 0 0 1-.25 1z" fill="var(--paper)"/></svg>
        800-555-0147</p>
      <p class="contact-web">
        <svg viewBox="0 0 24 24" aria-hidden="true"><circle cx="12" cy="12" r="10" fill="none" stroke="var(--gold)" stroke-width="2"/><path d="M2 12h20M12 2c3 3 3 17 0 20M12 2c-3 3-3 17 0 20" fill="none" stroke="var(--gold)" stroke-width="1.6"/></svg>
        www.corranridgeplex.example</p>
    </div>
  </div>
  <svg class="divider-stripe" viewBox="0 0 560 538" aria-hidden="true">
    <polygon points="527,0 533,0 453,538 447,538" fill="var(--paper)"/>
    <polygon points="533,0 552,0 472,538 453,538" fill="var(--maroon)"/>
  </svg>

  <div class="stamp-box"></div>
  <div class="address-line line-1"></div>
  <div class="address-line line-2"></div>
  <div class="partner-badge"></div>
  <div class="back-brand">
    <span class="brand-mark"></span>
    <div><p class="brand-name">CREDC</p><p class="brand-url">corranridgeplex.example</p></div>
  </div>
  <div class="location-map" role="img" aria-label="Regional map showing Doña Ana County between Arizona, Texas and Mexico"></div>
</section>

</body>
</html>
```